Haskell and Dunmore Ranch Insurance

Would like you all to design a logo for our Business cards and possible letterhead.
This business provides Ranch insurance for folks in Texas, New Mexico, and Oklahoma

Ggood stuff everybody, be sure to include email and Mobil for both of us on all designs

Thanks

Hello All

Wanted to let you all know i am going to extend deadline a few days, and add some more $$ to the budget

Reason: Give everybody a bit ,more time, and I added more money

Appreciate all of yalls hard work, will review and provide feed back hopefully today, been a little whacky with the holidays and all

```html
<!DOCTYPE html>
<html lang="en">
<head>
<meta charset="utf-8">
<title>Haskell and Dunmore – Stationery</title>
<link rel="stylesheet" href="https://fonts.googleapis.com/css2?family=Didact+Gothic&display=swap">
<style>
  :root {
    --backdrop: #34418f;
    --paper: #ffffff;
    --ink: #111111;
    --pink: #e8198a;
    --pink-dark: #b80d68;
    --pink-light: #ff62bd;
    --on-pink: #ffffff;
    --watermark: rgba(232, 25, 138, 0.16);
  }
  * { box-sizing: border-box; margin: 0; padding: 0; }
  html, body { width: 1200px; height: 1000px; overflow: hidden; }
  body {
    position: relative;
    background: var(--backdrop);
    font-family: "Didact Gothic", "Century Gothic", sans-serif;
    color: var(--ink);
  }

  /* ---------- Shared brand pieces ---------- */
  .brand { display: flex; align-items: center; gap: 14px; }
  .brand-dot {
    width: 34px; height: 34px; border-radius: 50%;
    background: var(--pink); flex: none;
  }
  .brand-name { font-size: 24px; color: var(--ink); white-space: nowrap; }
  .pink-gloss {
    background: linear-gradient(160deg, var(--pink-light) 0%, var(--pink) 35%, var(--pink-dark) 60%, var(--pink) 80%, var(--pink-light) 100%);
  }
  .phone-icon { width: 11px; height: 17px; flex: none; }

  /* ---------- Business cards ---------- */
  .card {
    position: absolute; left: 70px;
    width: 410px; height: 234px;
    background: var(--paper);
    box-shadow: 0 4px 12px rgba(0,0,0,0.35);
    overflow: hidden;
  }
  .card--dunmore-1 { top: 60px; }
  .card--dunmore-2 { top: 380px; }
  .card--haskell   { top: 700px; }
  .card .brand { position: absolute; left: 28px; top: 38px; }
  .card-rule {
    position: absolute; left: 0; right: 0; top: 92px; bottom: 0;
    background: var(--ink);
    clip-path: polygon(0 16px, 100% 0, 100% 100%, 0 100%);
  }
  .card-body {
    position: absolute; left: 0; right: 0; top: 100px; bottom: 0;
    clip-path: polygon(0 16px, 100% 0, 100% 100%, 0 100%);
    color: var(--on-pink);
  }
  .card-agent {
    position: absolute; right: 48px; top: 26px; text-align: center;
  }
  .card-agent .agent-name { font-size: 14px; text-decoration: underline; display: block; }
  .card-agent .agent-role { font-size: 12px; display: block; margin-top: 2px; }
  .card-contact {
    position: absolute; left: 28px; top: 44px;
    font-size: 12px; line-height: 1; list-style: none;
  }
  .card-contact li { display: flex; align-items: center; gap: 6px; height: 20px; }
  .card-contact .label { margin-right: 4px; }

  /* ---------- Letterhead ---------- */
  .letterhead {
    position: absolute; left: 560px; top: 50px;
    width: 580px; height: 900px;
    background: var(--paper);
    box-shadow: 0 4px 14px rgba(0,0,0,0.35);
    overflow: hidden;
  }
  .lh-top-band { position: absolute; left: 0; right: 0; top: 0; height: 58px; }
  .lh-header { position: absolute; left: 34px; right: 34px; top: 82px; }
  .lh-header .brand-dot { width: 46px; height: 46px; }
  .lh-header .brand-name { font-size: 42px; }
  .lh-subtitle {
    position: absolute; right: 0; top: 64px;
    font-size: 14px; font-weight: bold; letter-spacing: 0.3px;
  }
  .lh-header-rule { position: absolute; left: 0; right: 0; top: 168px; height: 12px; }
  .lh-watermark {
    position: absolute; left: 40px; right: 40px; top: 460px; height: 160px;
    display: flex; align-items: center; justify-content: center; gap: 20px;
  }
  .lh-watermark .mark-dot {
    width: 64px; height: 64px; border-radius: 50%;
    background: var(--watermark); flex: none;
  }
  .lh-watermark .mark-name { font-size: 36px; color: var(--watermark); white-space: nowrap; }
  .lh-footer-rule { position: absolute; left: 0; right: 0; bottom: 170px; height: 14px; }
  .lh-footer {
    position: absolute; left: 34px; right: 34px; bottom: 44px; height: 110px;
    font-size: 11px; line-height: 1.35;
  }
  .lh-links { position: absolute; left: 0; top: 8px; display: grid; grid-template-columns: 58px auto; row-gap: 4px; }
  .lh-links dt { font-weight: bold; }
  .lh-links .or { margin-left: 24px; }
  .lh-reach { position: absolute; right: 0; bottom: 6px; text-align: left; }
  .lh-reach p { display: flex; align-items: center; gap: 6px; height: 19px; }
  .lh-bottom-band { position: absolute; left: 0; right: 0; bottom: 0; height: 26px; }
</style>
</head>
<body>

<svg width="0" height="0" style="position:absolute" aria-hidden="true">
  <symbol id="icon-phone" viewBox="0 0 11 17">
    <rect x="0.5" y="0.5" width="10" height="16" rx="2" fill="#222" stroke="#888"/>
    <rect x="2" y="2.5" width="7" height="7" fill="#6b7fa8"/>
    <circle cx="5.5" cy="13" r="1.3" fill="#aaa"/>
  </symbol>
</svg>

<article class="card card--dunmore-1">
  <div class="brand"><span class="brand-dot"></span><span class="brand-name">Haskell and Dunmore</span></div>
  <div class="card-rule"></div>
  <div class="card-body pink-gloss">
    <div class="card-agent"><span class="agent-name">T. Wes Dunmore</span><span class="agent-role">Agent</span></div>
    <ul class="card-contact">
      <li><svg class="phone-icon"><use href="#icon-phone"/></svg>325-555-0187</li>
      <li><span class="label">Email:</span>wes@haskellanddunmore.com</li>
      <li><span class="label">Website:</span>www.haskellanddunmore.com</li>
      <li># 408 W Oak St. Ozona, TX 76943</li>
    </ul>
  </div>
</article>

<article class="card card--dunmore-2">
  <div class="brand"><span class="brand-dot"></span><span class="brand-name">Haskell and Dunmore</span></div>
  <div class="card-rule"></div>
  <div class="card-body pink-gloss">
    <div class="card-agent"><span class="agent-name">T. Wes Dunmore</span><span class="agent-role">Agent</span></div>
    <ul class="card-contact">
      <li><svg class="phone-icon"><use href="#icon-phone"/></svg>325-555-0187</li>
      <li><span class="label">Email:</span>wes@haskellanddunmore.com</li>
      <li><span class="label">Website:</span>www.haskellanddunmore.com</li>
      <li># 408 W Oak St. Ozona, TX 76943</li>
    </ul>
  </div>
</article>

<article class="card card--haskell">
  <div class="brand"><span class="brand-dot"></span><span class="brand-name">Haskell and Dunmore</span></div>
  <div class="card-rule"></div>
  <div class="card-body pink-gloss">
    <div class="card-agent"><span class="agent-name">Ray Haskell</span><span class="agent-role">Agent</span></div>
    <ul class="card-contact">
      <li><svg class="phone-icon"><use href="#icon-phone"/></svg>512-555-0149</li>
      <li><span class="label">Email:</span>haskellr@rnco.com</li>
      <li><span class="label">Website:</span>www.haskellanddunmore.com</li>
      <li># 408 W Oak St. Ozona, TX 76943</li>
    </ul>
  </div>
</article>

<article class="letterhead">
  <div class="lh-top-band pink-gloss"></div>
  <header class="lh-header">
    <div class="brand"><span class="brand-dot"></span><span class="brand-name">Haskell and Dunmore</span></div>
    <span class="lh-subtitle">LetterHead</span>
  </header>
  <div class="lh-header-rule pink-gloss"></div>

  <div class="lh-watermark" aria-hidden="true">
    <span class="mark-dot"></span><span class="mark-name">Haskell and Dunmore</span>
  </div>

  <div class="lh-footer-rule pink-gloss"></div>
  <footer class="lh-footer">
    <dl class="lh-links">
      <dt>Website:</dt><dd>www.haskellanddunmore.com</dd>
      <dt>Email:</dt><dd>haskellr@rnco.com <span class="or">or</span><br>wes@haskellanddunmore.com</dd>
    </dl>
    <div class="lh-reach">
      <p># 408 W Oak St. Ozona, TX 76943</p>
      <p><svg class="phone-icon"><use href="#icon-phone"/></svg>512-555-0149 or 325-555-0187</p>
    </div>
  </footer>
  <div class="lh-bottom-band pink-gloss"></div>
</article>

</body>
</html>
```